Brindlewave Systems Retractable Banner

Need a design for a retractable banner (approx. 63 inches x 24 inches) Provide us with different raw file types including: ai, png. We may end up ordering a banner that is larger or smaller so please ensure the design provided can be scaled accordingly.
Key Features:
One of the two logos shown below must be displayed (your choice). We can provide other file formats for the logo if needed.
Words that have to be shown:
Your *Data Collection Problems* End Here
Our technology transforms any building into an *IoT Smart Building*
Our *Monitoring and Alerting* capabilities give you full insight and control of your devices and buildings
Please note the words within *(stars) must be accentuated in some way, please use your creative freedom.
A design that fits the look and feel of our brand, as seen in our website here: https://brindlewavesys.example/ is encouraged

```html
<!DOCTYPE html>
<html lang="en">
<head>
<meta charset="utf-8">
<title>Brindlewave Systems – Retractable Banner</title>
<link rel="stylesheet" href="https://fonts.googleapis.com/css2?family=Saira+Condensed:wght@500;600;700&display=swap">
<style>
  :root {
    --teal-deep: #16636b;
    --teal-bright: #1fa7b5;
    --teal-text: #17666e;
    --ink: #0b0b0b;
    --rule: #a6a6a6;
    --paper: #ffffff;
    --sky-top: #b9d7e8;
    --sky-low: #e6f0f5;
    --city: #8fa9b8;
  }
  html, body {
    margin: 0;
    padding: 0;
    overflow: hidden;
    background: var(--paper);
  }
  .banner {
    position: relative;
    width: 1200px;
    height: 3110px;
    overflow: hidden;
    background: var(--paper);
    font-family: "Saira Condensed", "Arial Narrow", sans-serif;
    color: var(--ink);
  }
  .banner__shapes {
    position: absolute;
    inset: 0;
  }
  .brand {
    position: absolute;
    left: 170px;
    top: 285px;
    display: flex;
    align-items: center;
    gap: 28px;
  }
  .brand__dot {
    width: 90px;
    height: 90px;
    border-radius: 50%;
    background: var(--teal-bright);
  }
  .brand__name {
    font-size: 108px;
    font-weight: 700;
    color: var(--ink);
    line-height: 1;
    white-space: nowrap;
  }
  .message {
    position: absolute;
    left: 0;
    width: 1200px;
    margin: 0;
    text-align: center;
    font-weight: 500;
  }
  .accent {
    color: var(--teal-text);
    font-weight: 700;
  }
  .message--headline {
    top: 628px;
    font-size: 88px;
    line-height: 100px;
  }
  .message--monitoring {
    top: 1016px;
    font-size: 86px;
    line-height: 98.5px;
  }
  .message--iot {
    top: 1604px;
    font-size: 86px;
    line-height: 99px;
  }
  .rule {
    position: absolute;
    left: 110px;
    width: 980px;
    height: 6px;
    background: var(--rule);
  }
  .rule--first { top: 969px; }
  .rule--second { top: 1563px; }
  .web-address {
    position: absolute;
    right: 78px;
    top: 2815px;
    margin: 0;
    font-size: 88px;
    font-weight: 500;
    color: var(--paper);
    line-height: 1;
  }
</style>
</head>
<body>
<main class="banner">
  <svg class="banner__shapes" width="1200" height="3110" viewBox="0 0 1200 3110">
    <defs>
      <linearGradient id="cityTone" x1="0" y1="0" x2="0" y2="1">
        <stop offset="0" stop-color="var(--sky-top)"/>
        <stop offset="0.3" stop-color="var(--sky-low)"/>
        <stop offset="0.6" stop-color="var(--city)"/>
        <stop offset="1" stop-color="#6f8f7a"/>
      </linearGradient>
    </defs>
    <path class="header-band" d="M0,0 H1200 V151 C820,135 330,250 0,489 Z" fill="var(--teal-deep)"/>
    <path class="skyline-photo" role="img" aria-label="Photo of a waterfront city skyline with tall residential towers"
          d="M0,2112 C520,2115 920,2000 1200,1835 V2900 H0 Z" fill="url(#cityTone)"/>
    <path class="footer-wave" d="M0,2776 C520,2765 960,2650 1200,2474 V3110 H0 Z" fill="var(--teal-bright)"/>
    <path class="footer-band" d="M0,2850 C560,2842 985,2730 1200,2560 V3110 H0 Z" fill="var(--teal-deep)"/>
  </svg>

  <div class="brand">
    <span class="brand__dot"></span>
    <span class="brand__name">Brindlewave Systems</span>
  </div>

  <p class="message message--headline">Your<br><span class="accent">Data Collection Problems</span><br>End Here</p>

  <div class="rule rule--first"></div>

  <p class="message message--monitoring">Our <span class="accent">Monitoring and Alerting</span><br>capabilities make your buildings<br>energy efficient and give you<br>insight and full control<br>of your assets</p>

  <div class="rule rule--second"></div>

  <p class="message message--iot">Our technology transforms<br>any building into an<br><span class="accent">IoT Smart Building</span></p>

  <p class="web-address">brindlewavesys.example</p>
</main>
</body>
</html>
```